Creative Brief
Eastmoor Directorate - Bahrain
Business Cards + Stationary materials.
Simple
Tariq Yousef Al-Mansoori
Head of Financial Affairs
P.O. Box 37182, Awali. Kingdom of Bahrain
talmansoori@eastmoor-dir.example
www.eastmoor-dir.example
We would like the design to include the following colors : cyan, golden & silver. But we are open to new ideas that match our new logo.
Stationary items include :
- A4 letterhead ( would prefer the logo in the top middle section so that we can write the office name on either side of the A4 paper. We would like to use the attached watermark image ( you can change the color to match the theme )
- Notepad
- Presentation folder
- Envelopes ( A4, A3, basically the whole nine yards)
a short explanation on the attached files :
* ED Logo : main logo that represents our office (available in B&W and colored)
* Watermark : design we want as a watermark on the stationary
* Horizon : logo (available in different sizes) that should appear close to the address line and should appear on all stationary materials and business cards. This represents Bahrain horizon plan for economic development, more info can be found here : http://www.horizonplan.example/web/ , or http://wiki.example.org/wiki/Bahrain_Horizon_Plan
We would like to also point out that the back side of the business card MUST include the same information as the front but in Arabic language, you can find the translated info below.
Name : طارق يوسف المنصوري
Title : رئيس الموارد المالية
address :
ص.ب 37182، عوالي. مملكة البحرين
all the other info should be the same.
We wouldn't mind seeing different types of fonts as long as they are professional, serious and formal.
ED Logo : main logo that represents our office - in black and white
ED Logo : main logo that represents our office - colored
design we want as a watermark on the stationary
logo that should appear close to the address line and should appear on all stationary materials and business cards. This represents Bahrain horizon plan for economic development, more info can be found here : http://www.horizonplan.example/web/ ,or http://wiki.example.org/wiki/Bahrain_Horizon_Plan

```html
<!DOCTYPE html>
<html lang="en">
<head>
<meta charset="utf-8">
<title>Eastmoor Directorate – Stationery Set</title>
<link rel="stylesheet" href="https://fonts.googleapis.com/css2?family=Lato:wght@400;700;900&family=Noto+Naskh+Arabic:wght@400;700&display=swap">
<style>
  :root{
    --stage:#9c9c9c;
    --navy:#1f3f8f;
    --navy-deep:#142c6b;
    --gold:#b79a5b;
    --cyan-edge:#b9dcf4;
    --cyan-mid:#e6f2fb;
    --silver-edge:#cfcfcf;
    --silver-mid:#f6f6f6;
    --cream-edge:#efd7b0;
    --cream-mid:#fdf4e4;
    --ink:#3b3b3b;
    --rule:#a9a9a9;
    --paper:#ffffff;
  }
  *{box-sizing:border-box;margin:0;padding:0}
  html,body{width:1200px;height:619px;overflow:hidden;background:var(--stage)}
  body{font-family:"Lato",sans-serif;color:var(--ink)}
  .stage{position:relative;width:1200px;height:619px;overflow:hidden;background:var(--stage)}

  .item{position:absolute;box-shadow:0 1px 3px rgba(0,0,0,.35);overflow:hidden}
  .theme-cyan{background:radial-gradient(ellipse at 50% 45%,var(--paper) 0%,var(--cyan-mid) 35%,var(--cyan-edge) 100%)}
  .theme-silver{background:radial-gradient(ellipse at 50% 45%,var(--paper) 0%,var(--silver-mid) 35%,var(--silver-edge) 100%)}
  .theme-cream{background:radial-gradient(ellipse at 50% 45%,var(--paper) 0%,var(--cream-mid) 35%,var(--cream-edge) 100%)}

  .letterhead{top:24px;width:270px;height:356px}
  .letterhead--cyan{left:25px}
  .letterhead--silver{left:427px}
  .letterhead--fax{left:788px}

  .brand{position:absolute;display:flex;flex-direction:column;align-items:center;gap:2px}
  .brand__mark{width:14px;height:14px;border-radius:50%;border:1.5px solid var(--navy)}
  .brand__name{font-size:5px;font-weight:700;color:var(--navy);white-space:nowrap;letter-spacing:.2px}
  .letterhead .brand{top:8px;left:50%;transform:translateX(-50%)}

  .office-line{position:absolute;top:9px;left:9px;font-size:3.6px;line-height:5px;color:var(--ink)}

  .watermark{position:absolute;left:15%;top:36%;width:70%;height:15%;border-radius:50%;
    background:radial-gradient(ellipse,rgba(120,120,120,.16),rgba(120,120,120,0) 70%)}

  .swoosh{position:absolute;left:0;bottom:0;width:100%;height:34px;display:block}

  .fax-title{position:absolute;top:50px;left:16px;font-size:18px;font-weight:900;color:#222;letter-spacing:.5px}
  .fax-fields{position:absolute;top:82px;left:16px;right:16px;display:grid;grid-template-columns:1fr 1fr;column-gap:14px;row-gap:9px}
  .fax-field{display:flex;align-items:flex-end;gap:4px;font-size:4.5px;color:#444}
  .fax-field span{flex:1;border-bottom:.6px solid var(--rule);height:6px}
  .fax-checks{position:absolute;top:140px;left:16px;right:16px;display:flex;justify-content:space-between}
  .fax-check{display:flex;align-items:center;gap:2px;font-size:4px;color:#444}
  .fax-check i{width:5px;height:5px;border:.6px solid #555;border-radius:1px;display:block}

  .envelope{width:307px;height:160px}
  .envelope--back{top:396px}
  .envelope--front{top:424px}
  .env-cyan.envelope--back{left:29px}.env-cyan.envelope--front{left:55px}
  .env-silver.envelope--back{left:410px}.env-silver.envelope--front{left:436px}
  .env-cream.envelope--back{left:787px}.env-cream.envelope--front{left:813px}
  .flap{position:absolute;inset:0;width:100%;height:100%}
  .envelope--back .brand{top:6px;left:50%;transform:translateX(-50%)}
  .envelope--front .brand{top:8px;left:10px}
  .envelope--front .watermark{top:40%;left:20%;width:60%;height:22%}

  .card{width:125px;height:48px;background:var(--paper)}
  .card--front{left:1068px;top:108px}
  .card--back{left:1068px;top:192px}
  .card--logo{left:1068px;top:276px}
  .card .swoosh{height:12px}
  .card .brand{top:6px;right:8px}
  .card-person{position:absolute;top:8px;left:8px}
  .card-person__name{font-size:5px;font-weight:700;color:var(--navy)}
  .card-person__title{font-size:3.8px;color:var(--gold);margin-top:1px}
  .card-contacts{position:absolute;top:23px;left:8px;font-size:3.2px;line-height:4.4px;color:var(--ink)}
  .card--back{direction:rtl;font-family:"Noto Naskh Arabic",serif}
  .card--back .card-person{left:auto;right:8px}
  .card--back .card-contacts{left:auto;right:8px;direction:rtl}
  .card--back .brand{right:auto;left:8px}
  .card--logo .brand{top:10px;left:50%;right:auto;transform:translateX(-50%)}
  .card--logo .brand__mark{width:16px;height:16px}
  .card--logo .brand__name{font-size:5.5px}
</style>
</head>
<body>
<main class="stage">

  <svg width="0" height="0" style="position:absolute" aria-hidden="true">
    <defs>
      <symbol id="swoosh-band" viewBox="0 0 100 20" preserveAspectRatio="none">
        <path d="M0,9 Q45,22 100,6 L100,20 L0,20 Z" fill="var(--navy)"/>
        <path d="M0,5 Q45,19 100,3" fill="none" stroke="var(--gold)" stroke-width="1.2"/>
      </symbol>
    </defs>
  </svg>

  <!-- Letterheads -->
  <section class="item letterhead letterhead--cyan theme-cyan">
    <p class="office-line">Eastmoor Directorate<br>P.O. Box 37182, Awali</p>
    <div class="brand"><span class="brand__mark"></span><span class="brand__name">Eastmoor Directorate</span></div>
    <div class="watermark" role="img" aria-label="Faint calligraphic watermark of the directorate name"></div>
    <svg class="swoosh"><use href="#swoosh-band"/></svg>
  </section>

  <section class="item letterhead letterhead--silver theme-silver">
    <p class="office-line">Eastmoor Directorate<br>P.O. Box 37182, Awali</p>
    <div class="brand"><span class="brand__mark"></span><span class="brand__name">Eastmoor Directorate</span></div>
    <div class="watermark" role="img" aria-label="Faint calligraphic watermark of the directorate name"></div>
    <svg class="swoosh"><use href="#swoosh-band"/></svg>
  </section>

  <section class="item letterhead letterhead--fax theme-cream">
    <div class="brand" style="left:auto;right:10px;transform:none"><span class="brand__mark"></span><span class="brand__name">Eastmoor Directorate</span></div>
    <h1 class="fax-title">FAX</h1>
    <div class="fax-fields">
      <div class="fax-field">To<span></span></div>
      <div class="fax-field">From<span></span></div>
      <div class="fax-field">Fax<span></span></div>
      <div class="fax-field">Pages<span></span></div>
      <div class="fax-field">Phone<span></span></div>
      <div class="fax-field">Date<span></span></div>
      <div class="fax-field">Re<span></span></div>
      <div class="fax-field">CC<span></span></div>
    </div>
    <div class="fax-checks">
      <div class="fax-check"><i></i>Urgent</div>
      <div class="fax-check"><i></i>Review</div>
      <div class="fax-check"><i></i>Comment</div>
      <div class="fax-check"><i></i>Reply</div>
      <div class="fax-check"><i></i>Recycle</div>
    </div>
    <div class="watermark" role="img" aria-label="Faint calligraphic watermark of the directorate name"></div>
    <svg class="swoosh"><use href="#swoosh-band"/></svg>
  </section>

  <!-- Business cards -->
  <article class="item card card--front">
    <div class="card-person">
      <p class="card-person__name">Tariq Yousef Al-Mansoori</p>
      <p class="card-person__title">Head of Financial Affairs</p>
    </div>
    <p class="card-contacts">P.O. Box 37182, Awali. Kingdom of Bahrain<br>talmansoori@eastmoor-dir.example<br>www.eastmoor-dir.example</p>
    <div class="brand"><span class="brand__mark"></span></div>
    <svg class="swoosh"><use href="#swoosh-band"/></svg>
  </article>

  <article class="item card card--back">
    <div class="card-person">
      <p class="card-person__name">طارق يوسف المنصوري</p>
      <p class="card-person__title">رئيس الموارد المالية</p>
    </div>
    <p class="card-contacts">ص.ب 37182، عوالي. مملكة البحرين<br>talmansoori@eastmoor-dir.example</p>
    <div class="brand"><span class="brand__mark"></span></div>
    <svg class="swoosh"><use href="#swoosh-band"/></svg>
  </article>

  <article class="item card card--logo">
    <div class="brand"><span class="brand__mark"></span><span class="brand__name">Eastmoor Directorate</span></div>
    <svg class="swoosh"><use href="#swoosh-band"/></svg>
  </article>

  <!-- Envelopes -->
  <section class="item envelope envelope--back env-cyan theme-cyan">
    <svg class="flap" viewBox="0 0 100 100" preserveAspectRatio="none"><path d="M0,0 L50,48 L100,0" fill="none" stroke="#8aa9c2" stroke-width=".5"/></svg>
    <div class="brand"><span class="brand__mark"></span><span class="brand__name">Eastmoor Directorate</span></div>
  </section>
  <section class="item envelope envelope--front env-cyan theme-cyan">
    <div class="brand"><span class="brand__mark"></span><span class="brand__name">Eastmoor Directorate</span></div>
    <div class="watermark" role="img" aria-label="Faint calligraphic watermark of the directorate name"></div>
    <svg class="swoosh"><use href="#swoosh-band"/></svg>
  </section>

  <section class="item envelope envelope--back env-silver theme-silver">
    <svg class="flap" viewBox="0 0 100 100" preserveAspectRatio="none"><path d="M0,0 L50,48 L100,0" fill="none" stroke="#9a9a9a" stroke-width=".5"/></svg>
    <div class="brand"><span class="brand__mark"></span><span class="brand__name">Eastmoor Directorate</span></div>
  </section>
  <section class="item envelope envelope--front env-silver theme-silver">
    <div class="brand"><span class="brand__mark"></span><span class="brand__name">Eastmoor Directorate</span></div>
    <div class="watermark" role="img" aria-label="Faint calligraphic watermark of the directorate name"></div>
    <svg class="swoosh"><use href="#swoosh-band"/></svg>
  </section>

  <section class="item envelope envelope--back env-cream theme-cream">
    <svg class="flap" viewBox="0 0 100 100" preserveAspectRatio="none"><path d="M0,0 L50,48 L100,0" fill="none" stroke="#bda47a" stroke-width=".5"/></svg>
    <div class="brand"><span class="brand__mark"></span><span class="brand__name">Eastmoor Directorate</span></div>
  </section>
  <section class="item envelope envelope--front env-cream theme-cream">
    <div class="brand"><span class="brand__mark"></span><span class="brand__name">Eastmoor Directorate</span></div>
    <div class="watermark" role="img" aria-label="Faint calligraphic watermark of the directorate name"></div>
    <svg class="swoosh"><use href="#swoosh-band"/></svg>
  </section>

</main>
</body>
</html>
```